Harborline Crest Insurance Services

we are a high end insurance agency we specialize on Auto | Home | Business | Life looking for something professional and luxuries at the same time. if you guys need anything else please let me know.

Auto | Home | Business | Life must be under logo on the back with black background.

i want the back part to be black with our gold logo on it.

Target Market(s)

Auto | Home | Business | Life

Industry/Entity Type

Insurance Broker

Contact Information for Business Card

My logo is gold so a black in the back would be nice.

Font styles to use
Serif

Colors
000000

Requirements
Must have
• Big logo on the back with black background.

```html
<!DOCTYPE html>
<html lang="en">
<head>
<meta charset="utf-8">
<title>Harborline Crest Insurance Services — Business Card</title>
<link href="https://fonts.googleapis.com/css2?family=Cinzel:wght@400&family=Roboto+Condensed:wght@400&display=swap" rel="stylesheet">
<style>
  :root {
    --backdrop: #1b1b1b;
    --card-white: #ffffff;
    --card-black: #000000;
    --gold: #e8b92c;
    --text-light: #ffffff;
  }
  * { margin: 0; padding: 0; box-sizing: border-box; }
  html, body {
    width: 1200px;
    height: 1000px;
    overflow: hidden;
    background: var(--backdrop);
  }
  .canvas {
    position: relative;
    width: 1200px;
    height: 1000px;
  }
  .card {
    position: absolute;
    left: 330px;
    width: 540px;
    height: 330px;
    border-radius: 22px;
  }
  .card--front { top: 95px; background: var(--card-white); }
  .card--back  { top: 528px; background: var(--card-black); }

  .brand-mark {
    position: absolute;
    border-radius: 50%;
    background: var(--gold);
  }
  .brand-name {
    position: absolute;
    font-family: "Cinzel", "Times New Roman", serif;
    font-weight: 400;
    color: var(--gold);
    white-space: nowrap;
  }
  .brand-name__line { display: block; }
  .brand-name__main { font-size: 25px; line-height: 28px; }
  .brand-name__sub  { font-size: 12px; line-height: 16px; letter-spacing: 3.4px; }

  /* front */
  .card--front .brand-mark { left: 92px; top: 118px; width: 84px; height: 84px; }
  .card--front .brand-name { left: 212px; top: 136px; }

  /* back */
  .card--back .brand-mark { left: 220px; top: 52px; width: 100px; height: 100px; }
  .card--back .brand-name { left: 0; width: 100%; top: 176px; text-align: center; }

  .services {
    position: absolute;
    left: 0;
    width: 100%;
    top: 232px;
    text-align: center;
    font-family: "Roboto Condensed", "Arial Narrow", sans-serif;
    font-size: 29px;
    color: var(--text-light);
  }
</style>
</head>
<body>
  <main class="canvas">
    <section class="card card--front" aria-label="Card front">
      <span class="brand-mark" aria-hidden="true"></span>
      <h1 class="brand-name">
        <span class="brand-name__line brand-name__main">Harborline Crest</span>
        <span class="brand-name__line brand-name__sub">INSURANCE SERVICES</span>
      </h1>
    </section>

    <section class="card card--back" aria-label="Card back">
      <span class="brand-mark" aria-hidden="true"></span>
      <h2 class="brand-name">
        <span class="brand-name__line brand-name__main">Harborline Crest</span>
        <span class="brand-name__line brand-name__sub">INSURANCE SERVICES</span>
      </h2>
      <p class="services">Auto - Home - Business - Life</p>
    </section>
  </main>
</body>
</html>
```